Refresh of Business Card Design

Want to refresh the business card design with the new logo while adhering to style guide as attached. Would like to match feel of website www.durmackvinex.com

```html
<!DOCTYPE html>
<html lang="en">
<head>
<meta charset="utf-8">
<title>Durmack Vinex – Business Card</title>
<link rel="stylesheet" href="https://fonts.googleapis.com/css2?family=Barlow:wght@500&family=Arimo&display=swap">
<style>
  :root {
    --page: #ffffff;
    --brand-red: #e82244;
    --ink-black: #080808;
    --ring-grey: #b9b9b9;
    --text-white: #ffffff;
  }
  html, body {
    margin: 0;
    width: 1200px;
    height: 1200px;
    overflow: hidden;
    background: var(--page);
  }
  .canvas {
    position: relative;
    width: 1200px;
    height: 1200px;
  }
  .card {
    position: absolute;
    left: 26px;
    top: 235px;
    width: 1155px;
    height: 737px;
  }
  .card-bg {
    position: absolute;
    inset: 0;
    display: block;
  }
  .brand-name {
    position: absolute;
    left: 0;
    width: 1140px;
    top: 88px;
    text-align: center;
    font-family: "Barlow", sans-serif;
    font-weight: 500;
    font-size: 62px;
    letter-spacing: 6px;
    color: var(--text-white);
    margin: 0;
  }
  .holder {
    position: absolute;
    left: 52px;
    top: 534px;
    width: 340px;
    font-family: "Barlow", sans-serif;
    font-weight: 500;
    color: var(--text-white);
  }
  .holder-name {
    margin: 0;
    font-size: 52px;
    line-height: 1;
    font-weight: 500;
    white-space: nowrap;
  }
  .holder-role {
    margin: 6px 0 0;
    text-align: center;
    font-size: 30px;
    line-height: 1;
  }
  .website {
    position: absolute;
    left: 52px;
    top: 652px;
    margin: 0;
    font-family: "Arimo", sans-serif;
    font-size: 25px;
    color: var(--text-white);
  }
  .contact {
    position: absolute;
    right: 36px;
    top: 530px;
    margin: 0;
    text-align: right;
    font-family: "Barlow", sans-serif;
    font-weight: 500;
    font-size: 31px;
    line-height: 38.5px;
    color: var(--text-white);
    font-style: normal;
  }
</style>
</head>
<body>
<div class="canvas">
  <section class="card">
    <svg class="card-bg" width="1155" height="737" viewBox="0 0 1155 737" aria-hidden="true">
      <rect class="field-red" x="0" y="0" width="1155" height="737" fill="var(--brand-red)"/>
      <polygon class="field-black" points="1155,0 1155,737 0,737" fill="var(--ink-black)"/>
      <circle class="emblem-ring" cx="566" cy="369" r="205" fill="rgba(0,0,0,0.55)" stroke="var(--ring-grey)" stroke-width="12"/>
    </svg>

    <h1 class="brand-name">DURMACK VINEX</h1>

    <div class="holder">
      <p class="holder-name">DEAN HOLLIS</p>
      <p class="holder-role">SALES</p>
    </div>

    <p class="website">www.durmackvinex.com</p>

    <address class="contact">
      Cell:555.013.2748<br>
      P.o.box.40218 Carver. Tx70412<br>
      42 Lantern Dr Halvern, Texas, 70455<br>
      Twiter@durmack vinex.com
    </address>
  </section>
</div>
</body>
</html>
```